New, modern business card for growing audiology practice

We need a new business card for our audiology practice. Our logo and website have recently changed (more modern) and we want our business cards to reflect this change.
We conduct hearing tests, perform earwax removals, and fit & dispense hearing aids to our patients. We are a family owned practice in which the owner is the one who works directly with the patient. I have attached logos in various formats to use, as well as two ideas I found on this website; as well as a scanned copy of our current logo. Good luck!

Industry/Entity Type

Business

Contact Information for Business Card

Company name: Maplow Hearing Center
Provider name: Peter Mulvoy, Au.D. F/ISN
Phone number: (555) 318-6042
Address: 87 W. Linden Ave. Alder Falls, VT 05999
email: maplowhearing@postvale.net
website: maplowhearing.com

Colors
000000
aaaaaa
dbdbdb
cacaca
9bcb3c
afd23c
cadf82
b1b1b1

Requirements
Must have
• My card must include information in the "details" section. In the attached images, I found a few that I liked and I would like to model after - "brisk tumblin'" and "Sound Wellness Center".
• Must be horizontal.
• Must include logos provided. I uploaded them in various file formats and various ways.
• Must match logo font, if possible, if not, please get as close as you can.
Nice to have
• I really like the idea of having a color on one side with just the logo and company name and the contact information and provider name on the other side. I also really like the idea of having the main color dominating on the logo/company side with accent of that same color on the contact side of the card.
Should not have
• Must not be vertical.

```html
<!DOCTYPE html>
<html lang="en">
<head>
<meta charset="utf-8">
<title>Maplow Hearing Center – Business Card</title>
<link rel="stylesheet" href="https://fonts.googleapis.com/css2?family=Lato:wght@400&family=Tinos&display=swap">
<style>
  :root {
    --green: #afd23c;
    --ink: #2f3436;
    --black: #000000;
    --paper: #ffffff;
  }
  html, body {
    margin: 0;
    padding: 0;
    overflow: hidden;
    background: var(--paper);
  }
  .canvas {
    position: relative;
    width: 1200px;
    height: 1200px;
    overflow: hidden;
    background: var(--paper);
  }
  .brand-dot {
    position: absolute;
    border-radius: 50%;
    background: var(--green);
  }
  .brand-name {
    position: absolute;
    margin: 0;
    font-family: "Lato", sans-serif;
    font-weight: 400;
    color: var(--ink);
    letter-spacing: -0.01em;
    text-transform: uppercase;
  }
  .brand-name span {
    position: absolute;
    left: 0;
    white-space: nowrap;
  }
  /* large brand lockup */
  .hero .brand-dot { left: 254px; top: 199px; width: 240px; height: 240px; }
  .hero .brand-name { left: 526px; top: 0; font-size: 89px; line-height: 1; }
  .hero .brand-name span:nth-child(1) { top: 191px; }
  .hero .brand-name span:nth-child(2) { top: 273px; }
  .hero .brand-name span:nth-child(3) { top: 356px; }

  /* card lockup */
  .card .brand-dot { left: 223px; top: 806px; width: 140px; height: 140px; }
  .card .brand-name { left: 372px; top: 0; font-size: 35px; line-height: 1; }
  .card .brand-name span:nth-child(1) { top: 806px; }
  .card .brand-name span:nth-child(2) { top: 843px; }
  .card .brand-name span:nth-child(3) { top: 880px; }

  .provider {
    position: absolute;
    left: 590px;
    top: 736px;
    margin: 0;
    font-family: "Tinos", serif;
  }
  .provider-name {
    display: block;
    color: var(--green);
    font-size: 31px;
    line-height: 36px;
  }
  .provider-role {
    display: block;
    color: var(--black);
    font-size: 22px;
    line-height: 28px;
  }
  .contact-list {
    position: absolute;
    left: 586px;
    top: 862px;
    margin: 0;
    padding: 0;
    list-style: none;
    font-family: "Tinos", serif;
    font-size: 19px;
    color: var(--black);
  }
  .contact-item {
    position: relative;
    height: 38px;
    padding-left: 39px;
    line-height: 38px;
  }
  .contact-item:nth-child(1) { height: 42px; }
  .contact-icon {
    position: absolute;
    left: 0;
    top: 5px;
    width: 30px;
    height: 28px;
  }
  .accent-band {
    position: absolute;
    left: 194px;
    top: 1078px;
    width: 807px;
    height: 28px;
    background: var(--green);
  }
</style>
</head>
<body>
<main class="canvas">
  <section class="hero">
    <div class="brand-dot"></div>
    <h1 class="brand-name"><span>Maplow</span><span>Hearing</span><span>Center</span></h1>
  </section>

  <section class="card">
    <div class="brand-dot"></div>
    <p class="brand-name"><span>Maplow</span><span>Hearing</span><span>Center</span></p>

    <p class="provider">
      <span class="provider-name">Peter Mulvoy, Au.D. F/ISN</span>
      <span class="provider-role">Owner - Audiologist</span>
    </p>

    <ul class="contact-list">
      <li class="contact-item">
        <svg class="contact-icon" viewBox="0 0 30 30" aria-hidden="true">
          <path d="M15 28 C10 20 6 15 6 10 a9 9 0 0 1 18 0 c0 5 -4 10 -9 18z" fill="none" stroke="#000" stroke-width="1.4"/>
          <circle cx="15" cy="10" r="3.5" fill="none" stroke="#000" stroke-width="1.4"/>
        </svg>
        87 W. Linden Ave. Alder Falls, VT 05999
      </li>
      <li class="contact-item">
        <svg class="contact-icon" viewBox="0 0 30 30" aria-hidden="true">
          <path d="M2 10 C2 4 28 4 28 10 L28 13 L22 13 L22 10 L8 10 L8 13 L2 13 Z" fill="#000"/>
          <path d="M7 14 L23 14 L27 27 L3 27 Z" fill="#000"/>
          <circle cx="15" cy="20" r="4" fill="#fff"/>
          <circle cx="15" cy="20" r="1.8" fill="#000"/>
        </svg>
        (555) 318-6042
      </li>
      <li class="contact-item">
        <svg class="contact-icon" viewBox="0 0 30 30" aria-hidden="true">
          <rect x="1.5" y="5" width="27" height="20" fill="none" stroke="#000" stroke-width="1.6"/>
          <path d="M1.5 5 L15 17 L28.5 5 M1.5 25 L11 14 M28.5 25 L19 14" fill="none" stroke="#000" stroke-width="1.4"/>
        </svg>
        maplowhearing@postvale.net
      </li>
      <li class="contact-item">
        <svg class="contact-icon" viewBox="0 0 30 30" aria-hidden="true">
          <g fill="none" stroke="#000" stroke-width="1.2">
            <circle cx="15" cy="15" r="13"/>
            <ellipse cx="15" cy="15" rx="6" ry="13"/>
            <path d="M15 2 V28 M2 15 H28 M4 8 H26 M4 22 H26"/>
          </g>
        </svg>
        maplowhearing.com
      </li>
    </ul>

    <div class="accent-band"></div>
  </section>
</main>
</body>
</html>
```